14 years in business and its time for a new look and feel brochure and business cards!

We are looking to create a brochure that is professional and eye catching to bring in new commercial business. After14 years in business we have finally redone our logo and it is time to get a brochure completed as well. The logo that should be used is the one that says Inc. We want this new brochure to appeal to corporate property management companies and smaller apartment complexes. We want it to look rich and have the same high quality our work has.

Target Market(s)

property management companies and apartment complexes in the DMV.

Industry/Entity Type

Construction Company

Contact Information for Business Card

Logo
Dovid Markel
CEO
Mobile 410-555-0187
Office 410-555-0142
Address 3417 Harlow Lane Suite C Baltimore, MD 21290
Email DM@BrightCoatProsInc.example

Font styles to use
Sans Serif

Requirements
Must have
• Want the background to be black and silver gradient. Will be printing on high gloss and would like for it to be rich looking.
• brochure will be 8.5x11. open minded in terms of the fold, how it looks best with the design provided will determine that. Can be bi-fold, try-fold or z-fold.
• Content for brochure:About us
• Founded in 2003, BrightCoat Pros Inc. was the vision of Dovid Markel, with a commitment to becoming the premier renovator and developer of residential and commercial properties in the DMV. Today, BrightCoat Pros Inc. is widely respected for their gold standard in quality and efficiency and continues to grow by attracting the highest level of professionals with knowledge and experience in our field.
• BrightCoat Pros Inc.’s most valuable asset is our team members. The efforts they put forth are the key to meeting our standards and providing all of our valued clients with the highest quality of service. Leading our wonderful team members is a group of management like no other. With years of experience, the power to motivate and the keen eye to ensure top quality, our team of experts focus all of their energy to exceed our client’s expectations.
• Our Mission
• We strive to provide timely delivery, the highest level of quality and value on every project. We offer unsurpassed dedication to maintain our working relationships and consistently deliver the best service to ensure our clients success.
• Property Renovations
• BrightCoat Pros Inc. has been responsible for coordinating the construction and renovation of many projects, including all parts of a building’s interior and exterior. Well known for attention to details, quality and timely execution, BrightCoat Pros Inc. has managed and executed more than 4,000 turnovers and over 150 projects in the last 3 years alone.
• Renovations not only improve the appeal and marketability of your property, but also add value. Interior and exterior renovations help make any property more functional, energy-efficient and enable you to keep up with what your market demands. From the smallest change of a door knob to a complete kitchen overhaul, these are the things that make all the difference in your property. We are committed to deliver great value, and we do that by ensuring that our experts are involved in the renovation process, providing input and quality maintenance throughout the entire renovation.
• Services Include
• Painting
• Flooring
• Sub-Flooring
• Crown molding
• Siding & Wood Replacement
• Trim & Carpentry Work
• Punches
• Decks
• Power wash
• Concrete & Paving
• Turnovers including plumbing and electric
• Kitchen overhauls
• We offer first time clients a free apartment paint or punch on us to show you the quality you can always expect!
• Call today to schedule your first-time paint or punch at 410-555-0142.

```html
<!DOCTYPE html>
<html lang="en">
<head>
<meta charset="utf-8">
<title>BrightCoat Pros Inc. — Brochure &amp; Business Cards</title>
<link href="https://fonts.googleapis.com/css2?family=Montserrat:wght@500;700;800&family=Lato:wght@400;700&display=swap" rel="stylesheet">
<style>
:root{
  --stage:#c6ecfb;
  --black:#111;
  --charcoal:#2a2a2a;
  --silver:#c9c9c9;
  --silver-light:#f2f2f2;
  --grey-band:#6e6e72;
  --text-light:#e8e8e8;
  --text-muted:#b5b5b5;
  --photo-warm:#b9a58a;
  --photo-cool:#8f8a84;
}
*{box-sizing:border-box;margin:0;padding:0}
html,body{width:1200px;height:1200px;overflow:hidden;background:var(--stage)}
body{position:relative;font-family:"Lato",sans-serif;color:var(--text-light)}
.sheet{position:absolute;display:flex;box-shadow:0 10px 24px rgba(0,0,0,.25)}
.sheet--outside{left:30px;top:30px}
.sheet--inside{left:210px;top:630px}
.panel{position:relative;width:260px;height:540px;overflow:hidden;
  background:linear-gradient(160deg,#3a3a3a 0%,var(--black) 35%,#1b1b1b 70%,#444 100%)}
.panel + .panel{border-left:1px solid #000}
.photo{position:absolute;left:0;top:0}
.brand{display:flex;align-items:center;justify-content:center;gap:7px;
  font-family:"Montserrat",sans-serif;font-weight:800;color:#fff;letter-spacing:.5px}
.brand__dot{width:16px;height:16px;border-radius:50%;background:#fff;flex:none}
.heading{font-family:"Montserrat",sans-serif;font-weight:700;font-size:9px;letter-spacing:1px;color:#fff;text-transform:uppercase}
.body-copy{font-size:6.6px;line-height:1.42;color:var(--text-muted);text-align:justify;margin-top:5px}
/* outside flap */
.about{position:absolute;left:18px;right:18px;top:188px}
.about .heading{margin-top:10px}
.about .heading:first-child{margin-top:0}
/* back panel */
.offer{position:absolute;left:14px;right:14px;top:50px;text-align:center;font-size:10px;line-height:1.35}
.offer strong{font-family:"Montserrat",sans-serif;font-weight:700;color:var(--silver);letter-spacing:1px;font-size:12px}
.offer small{display:block;font-size:8.5px;color:var(--silver)}
.divider{position:absolute;left:30px;right:30px;top:178px;height:1px;background:linear-gradient(90deg,transparent,#777,transparent)}
.call{position:absolute;left:14px;right:14px;top:196px;text-align:center;font-size:10px;line-height:1.4}
.call strong{font-family:"Montserrat",sans-serif;font-weight:700;color:var(--silver);letter-spacing:1px;font-size:12px}
.call .phone{display:flex;align-items:center;justify-content:center;gap:6px;margin-top:8px;
  font-family:"Montserrat",sans-serif;font-weight:800;font-size:13px;color:#fff}
.back-brand{position:absolute;left:0;right:0;top:335px;font-size:13px}
.contact-list{position:absolute;left:10px;right:10px;top:385px;text-align:center;font-size:7.5px;font-weight:700;color:#fff}
.contact-list li{list-style:none;display:flex;flex-direction:column;align-items:center;gap:3px;margin-bottom:10px}
/* cover */
.cover-brand{position:absolute;left:0;right:0;top:70px;font-size:15px}
.tagline{position:absolute;left:0;right:0;top:440px;height:62px;text-align:center;color:#111;
  background:linear-gradient(180deg,#fff,#dcdcdc);font-family:"Montserrat",sans-serif;font-weight:800;padding-top:8px}
.tagline span{display:block;font-size:21px;letter-spacing:1px;line-height:1}
.tagline em{font-style:normal;display:block;font-size:14px;font-weight:700;margin-top:4px}
.web-band{position:absolute;left:0;right:0;bottom:0;height:38px;background:var(--grey-band);
  font-size:7px;letter-spacing:3px;color:#ddd;display:flex;align-items:center;justify-content:center}
/* inside */
.renov{position:absolute;left:18px;right:18px;top:22px}
.renov .body-copy{font-size:6.8px}
.services-title{position:absolute;left:0;right:0;top:28px;text-align:center}
.service-grid{position:absolute;left:14px;right:14px;display:grid;grid-template-columns:1fr 1fr;gap:16px 10px;list-style:none}
.service-grid--a{top:62px}
.service-grid--b{top:30px}
.service{display:flex;flex-direction:column;align-items:center;gap:5px;text-align:center;font-size:7.5px;color:#ddd;line-height:1.25}
.service__icon{width:22px;height:16px;border:1.5px solid #fff;border-radius:3px}
.service__icon--round{border-radius:50%;width:18px;height:18px}
/* cards */
.card{position:absolute;left:830px;width:340px;height:195px;overflow:hidden;box-shadow:0 8px 18px rgba(0,0,0,.25);
  background:linear-gradient(160deg,#3a3a3a,var(--black) 45%,#222 100%)}
.card--front{top:95px}
.card--back{top:330px}
.card__arc{position:absolute;left:0;top:0}
.card__brand{position:absolute;left:18px;top:82px;font-size:12px}
.card__person{position:absolute;right:18px;top:22px;text-align:right;font-family:"Montserrat",sans-serif}
.card__person b{display:block;font-size:10px;font-weight:700;color:#fff}
.card__person span{font-size:8.5px;color:#ccc}
.card__contacts{position:absolute;right:18px;top:68px;list-style:none;text-align:right;font-size:7.5px;color:#eee}
.card__contacts li{display:flex;align-items:center;justify-content:flex-end;gap:7px;height:19px}
.card--back .brand{position:absolute;left:0;right:0;top:78px;font-size:17px}
.card--back .web{position:absolute;left:0;right:0;bottom:24px;text-align:center;font-size:7px;letter-spacing:2.5px;color:#ccc}
</style>
</head>
<body>

<!-- Outside of the tri-fold -->
<section class="sheet sheet--outside" aria-label="Brochure outside">
  <article class="panel panel--about">
    <svg class="photo" width="260" height="180" role="img" aria-label="Photo of a hallway under renovation with drywall and tools">
      <defs><linearGradient id="hall" x1="0" y1="0" x2="1" y2="1"><stop offset="0" stop-color="#e8e4de"/><stop offset="1" stop-color="#9f968a"/></linearGradient></defs>
      <path d="M0,0 H250 Q230,125 0,165 Z" fill="url(#hall)"/>
      <path d="M250,0 Q230,125 0,165" fill="none" stroke="#d8d8d8" stroke-width="6"/>
    </svg>
    <div class="about">
      <h2 class="heading">About us</h2>
      <p class="body-copy">Founded in 2003, BrightCoat Pros Inc. was the vision of Dovid Markel, with a commitment to becoming the premier renovator and developer of residential and commercial properties in the DMV. Today, BrightCoat Pros Inc. is widely respected for their gold standard in quality and efficiency and continues to grow by attracting the highest level of professionals with knowledge and experience in our field.</p>
      <p class="body-copy">BrightCoat Pros Inc.’s most valuable asset is our team members. The efforts they put forth are the key to meeting our standards and providing all of our valued clients with the highest quality of service. Leading our wonderful team members is a group of management like no other. With years of experience, the power to motivate and the keen eye to ensure top quality, our team of experts focus all of their energy to exceed our client’s expectations.</p>
      <h2 class="heading">Our mission</h2>
      <p class="body-copy">We strive to provide timely delivery, the highest level of quality and value on every project. We offer unsurpassed dedication to maintain our working relationships and consistently deliver the best service to ensure our clients success.</p>
    </div>
  </article>

  <article class="panel panel--back">
    <p class="offer"><strong>WE OFFER</strong><br>first time clients a<br><strong>FREE APARTMENT</strong><br>paint or punch on us<small>TO SHOW YOU THE QUALITY</small>you can always expect!</p>
    <div class="divider"></div>
    <p class="call"><strong>CALL TODAY</strong><br>to schedule your<br><strong>FIRST-TIME</strong><br>paint or punch at
      <span class="phone"><svg width="12" height="12" viewBox="0 0 24 24"><path d="M6 2h4l2 5-3 2a12 12 0 0 0 6 6l2-3 5 2v4a2 2 0 0 1-2 2A18 18 0 0 1 4 4a2 2 0 0 1 2-2z" fill="#fff"/></svg>410-555-0142</span></p>
    <div class="brand back-brand"><span class="brand__dot"></span>BRIGHTCOAT PROS</div>
    <ul class="contact-list">
      <li><svg width="11" height="9" viewBox="0 0 22 16"><rect x="1" y="1" width="20" height="14" fill="none" stroke="#fff" stroke-width="2"/><path d="M1 1l10 8 10-8" fill="none" stroke="#fff" stroke-width="2"/></svg>contact@brightcoatprosinc.example</li>
      <li><svg width="11" height="11" viewBox="0 0 22 22"><circle cx="11" cy="11" r="9" fill="none" stroke="#fff" stroke-width="2"/><path d="M2 11h18M11 2c-5 6-5 12 0 18M11 2c5 6 5 12 0 18" fill="none" stroke="#fff" stroke-width="1.5"/></svg>www.brightcoatprosinc.example</li>
      <li><svg width="11" height="10" viewBox="0 0 22 20"><path d="M11 1L1 10h3v9h5v-6h4v6h5v-9h3z" fill="#fff"/></svg>3417 Harlow Lane Baltimore, Maryland</li>
    </ul>
  </article>

  <article class="panel panel--cover">
    <div class="brand cover-brand"><span class="brand__dot"></span>BRIGHTCOAT PROS</div>
    <svg class="photo" width="260" height="445" role="img" aria-label="Photo of a renovated kitchen with white cabinets, tiled backsplash and stainless appliances">
      <defs><linearGradient id="kitchen" x1="0" y1="0" x2="1" y2="1"><stop offset="0" stop-color="#e9e2d6"/><stop offset=".55" stop-color="#8a8178"/><stop offset="1" stop-color="#cfc8bf"/></linearGradient></defs>
      <path d="M0,310 Q70,195 260,180 V445 H0 Z" fill="url(#kitchen)"/>
      <path d="M0,310 Q70,195 260,180" fill="none" stroke="#d4d4d4" stroke-width="7"/>
    </svg>
    <div class="tagline"><span>A STEP</span><em>Above The Rest</em></div>
    <div class="web-band">www.brightcoatprosinc.example</div>
  </article>
</section>

<!-- Business cards -->
<section class="card card--front" aria-label="Business card front">
  <svg class="card__arc" width="340" height="195" aria-hidden="true">
    <path d="M0,22 Q120,2 340,10" fill="none" stroke="#fff" stroke-width="3"/>
    <path d="M0,195 Q60,150 340,160 V195 Z" fill="#d9d9d9"/>
    <path d="M0,195 Q70,162 340,172 V195 Z" fill="#111"/>
  </svg>
  <div class="brand card__brand"><span class="brand__dot"></span>BRIGHTCOAT PROS</div>
  <div class="card__person"><b>Your Name</b><span>Your Designation</span></div>
  <ul class="card__contacts">
    <li>410-555-0142<svg width="10" height="10" viewBox="0 0 24 24"><path d="M6 2h4l2 5-3 2a12 12 0 0 0 6 6l2-3 5 2v4a2 2 0 0 1-2 2A18 18 0 0 1 4 4a2 2 0 0 1 2-2z" fill="#fff"/></svg></li>
    <li>contact@brightcoatprosinc.example<svg width="10" height="8" viewBox="0 0 22 16"><rect x="1" y="1" width="20" height="14" fill="none" stroke="#fff" stroke-width="2"/><path d="M1 1l10 8 10-8" fill="none" stroke="#fff" stroke-width="2"/></svg></li>
    <li>www.brightcoatprosinc.example<svg width="10" height="10" viewBox="0 0 22 22"><circle cx="11" cy="11" r="9" fill="none" stroke="#fff" stroke-width="2"/><path d="M2 11h18M11 2c-5 6-5 12 0 18M11 2c5 6 5 12 0 18" fill="none" stroke="#fff" stroke-width="1.5"/></svg></li>
    <li>3417 Harlow Lane Baltimore, Maryland<svg width="10" height="9" viewBox="0 0 22 20"><path d="M11 1L1 10h3v9h5v-6h4v6h5v-9h3z" fill="#fff"/></svg></li>
  </ul>
</section>

<section class="card card--back" aria-label="Business card back">
  <div class="brand"><span class="brand__dot"></span>BRIGHTCOAT PROS</div>
  <p class="web">www.brightcoatprosinc.example</p>
</section>

<!-- Inside of the tri-fold -->
<section class="sheet sheet--inside" aria-label="Brochure inside">
  <article class="panel panel--renovations">
    <div class="renov">
      <h2 class="heading">Property renovations</h2>
      <p class="body-copy">BrightCoat Pros Inc. has been responsible for coordinating the construction and renovation of many projects, including all parts of a building’s interior and exterior. Well known for attention to details, quality and timely execution, BrightCoat Pros Inc. has managed and executed more than 4,000 turnovers and over 150 projects in the last 3 years alone.</p>
      <p class="body-copy">Renovations not only improve the appeal and marketability of your property, but also add value. Interior and exterior renovations help make any property more functional, energy-efficient and enable you to keep up with what your market demands. From the smallest change of a door knob to a complete kitchen overhaul, these are the things that make all the difference in your property. We are committed to deliver great value, and we do that by ensuring that our experts are involved in the renovation process, providing input and quality maintenance throughout the entire renovation.</p>
    </div>
    <svg class="photo" width="260" height="540" role="img" aria-label="Photo of an interior room with fresh drywall under renovation">
      <defs><linearGradient id="room" x1="0" y1="0" x2="1" y2="1"><stop offset="0" stop-color="#e6e6e6"/><stop offset="1" stop-color="#a9a9a6"/></linearGradient></defs>
      <path d="M0,345 Q160,320 260,395 V540 H0 Z" fill="url(#room)"/>
      <path d="M0,345 Q160,320 260,395" fill="none" stroke="#d4d4d4" stroke-width="6"/>
    </svg>
  </article>

  <article class="panel panel--services">
    <h2 class="heading services-title">Services include</h2>
    <ul class="service-grid service-grid--a">
      <li class="service"><span class="service__icon"></span>Painting</li>
      <li class="service"><span class="service__icon"></span>Flooring</li>
      <li class="service"><span class="service__icon"></span>Sub-Flooring</li>
      <li class="service"><span class="service__icon service__icon--round"></span>Crown molding</li>
      <li class="service"><span class="service__icon"></span>Siding &amp; Wood Replacement</li>
      <li class="service"><span class="service__icon service__icon--round"></span>Trim &amp; Carpentry Work</li>
    </ul>
  </article>

  <article class="panel panel--services-more">
    <ul class="service-grid service-grid--b">
      <li class="service"><span class="service__icon service__icon--round"></span>Punches</li>
      <li class="service"><span class="service__icon"></span>Decks</li>
      <li class="service"><span class="service__icon service__icon--round"></span>Power wash</li>
      <li class="service"><span class="service__icon"></span>Concrete &amp; Paving</li>
      <li class="service"><span class="service__icon"></span>Turnovers including plumbing and electric</li>
      <li class="service"><span class="service__icon"></span>Kitchen overhauls</li>
    </ul>
  </article>

  <svg style="position:absolute;left:260px;top:0" width="520" height="540" role="img" aria-label="Photo of a brick building with a new wooden deck and railings">
    <defs><linearGradient id="deck" x1="0" y1="0" x2="1" y2="1"><stop offset="0" stop-color="#a35b44"/><stop offset=".5" stop-color="#c9b08a"/><stop offset="1" stop-color="#7b5a42"/></linearGradient></defs>
    <path d="M0,540 Q180,330 520,250 V540 Z" fill="url(#deck)"/>
    <path d="M0,540 Q180,330 520,250" fill="none" stroke="#d4d4d4" stroke-width="7"/>
  </svg>
</section>

</body>
</html>
```